Tavrin Telecom Corporate Website & Social Branding

We are looking for a new website for our startup telecom which provides UCaaS, SD-WAN, Business SMS/MMS, Video Conferencing, Managed Network Service & more.

Target Market(s)

Small offices from 1-250 users

Industry/Entity Type

Telecomunications

Coding

Coded - Design and coding required

Colors
0054AA
0677BA
7BADD7
CADEEF
E8F1F8

```html
<!DOCTYPE html>
<html lang="en">
<head>
<meta charset="utf-8">
<title>Tavrin Telecom</title>
<link href="https://fonts.googleapis.com/css2?family=Poppins:ital,wght@0,400;0,500;0,600;0,700;0,800;1,700;1,800&display=swap" rel="stylesheet">
<style>
:root{
  --navy:#0054AA;
  --blue:#0677BA;
  --sky:#7BADD7;
  --pale:#CADEEF;
  --mist:#E8F1F8;
  --ink:#1b1f2a;
  --grey:#6b7280;
  --dark:#0b1a33;
  --white:#ffffff;
}
*{box-sizing:border-box;margin:0;padding:0}
html,body{width:1200px;height:4132px;overflow:hidden}
body{font-family:"Poppins",sans-serif;color:var(--ink);background:var(--white);font-size:12px;line-height:1.6}
a{color:inherit;text-decoration:none}
.btn{display:inline-block;background:var(--blue);color:var(--white);font-weight:600;font-size:10px;letter-spacing:.5px;padding:9px 20px;border-radius:20px;text-transform:uppercase}
.eyebrow{color:var(--blue);font-weight:600;font-size:11px;letter-spacing:1px;text-transform:uppercase}
.heading{font-weight:800;font-style:italic;font-size:36px;color:var(--ink);line-height:1.2}
.lead{color:var(--grey);font-size:12px;max-width:560px;margin:10px auto 0}
.center{text-align:center}

/* header */
.site-header{position:relative;height:100px;background:var(--white)}
.topbar{position:absolute;right:0;top:0;width:760px;height:34px;background:var(--blue);border-bottom-left-radius:34px;display:flex;justify-content:flex-end;align-items:center;gap:36px;padding-right:60px;color:var(--white);font-size:10px}
.topbar span{display:flex;align-items:center;gap:6px}
.logo{position:absolute;left:60px;top:20px;display:flex;align-items:center;gap:10px}
.logo-dot{width:34px;height:34px;border-radius:50%;background:var(--blue)}
.logo-name{font-weight:700;font-size:22px;color:var(--navy);line-height:1}
.nav{position:absolute;left:440px;top:56px;display:flex;gap:40px;font-size:11px;font-weight:500}
.nav .active{color:var(--blue)}
.nav-cta{position:absolute;right:60px;top:50px}

/* hero */
.hero{position:relative;height:520px;overflow:hidden}
.hero-photo{position:absolute;inset:0;background:linear-gradient(90deg,#f3f4f6 0%,#e6e9ee 40%,#c9ccd2 70%,#a9a39b 100%)}
.hero-text{position:absolute;left:60px;top:110px;width:420px}
.hero-text .eyebrow{font-size:14px}
.hero-title{font-weight:800;font-size:44px;line-height:1.1;color:var(--navy);margin:6px 0 14px}
.hero-text p{color:#4b5563;font-size:12px;margin-bottom:20px}
.hero-curve{position:absolute;left:0;bottom:0;width:1200px;height:90px}

/* services */
.services{height:600px;padding-top:90px;position:relative}
.cards{display:flex;justify-content:center;gap:14px;margin-top:36px}
.card{width:208px;height:280px;background:var(--white);border-radius:6px;box-shadow:0 6px 24px rgba(0,40,90,.12);text-align:center;padding:34px 18px 0}
.card svg{width:58px;height:58px}
.card h3{font-size:14px;font-weight:700;margin:16px 0 10px}
.card p{font-size:10px;color:var(--grey);line-height:1.6}
.card .more{display:block;margin-top:14px;font-size:9px;font-weight:700;color:var(--blue);text-transform:uppercase}
.card.featured{background:var(--blue);color:var(--white);margin-top:-14px;height:294px}
.card.featured p,.card.featured .more{color:var(--white)}
.services .btn{margin-top:36px}

/* about */
.about{height:520px;position:relative;background:var(--mist);overflow:hidden}
.about-photo{position:absolute;left:150px;top:80px;width:330px;height:330px;border-radius:50%;background:radial-gradient(circle at 50% 40%,#d9c2ad 0%,#b9a896 30%,#e9eef4 60%,#f6f8fb 100%);border:10px solid var(--white);box-shadow:0 0 0 4px var(--pale)}
.about-text{position:absolute;left:610px;top:110px;width:480px}
.about-text .heading{margin:4px 0 12px}
.about-text p{color:var(--grey);font-size:11px;margin-bottom:10px}
.about-text .btn{margin-top:12px}

/* features */
.features{height:500px;padding-top:70px}
.feature-row{display:flex;justify-content:center;gap:30px;margin-top:44px}
.feature{width:250px;text-align:center}
.feature-icon{width:110px;height:110px;margin:0 auto;border-radius:50%;background:var(--mist);display:flex;align-items:center;justify-content:center;position:relative}
.feature-icon::before{content:"";position:absolute;inset:-6px;border-radius:50%;border:3px solid var(--blue);border-right-color:transparent;border-top-color:transparent}
.feature h3{font-size:15px;font-weight:700;margin:24px 0 8px}
.feature p{font-size:10px;color:var(--grey)}

/* cta */
.cta{height:340px;position:relative}
.cta-photo{position:absolute;left:60px;right:60px;top:30px;bottom:30px;background:linear-gradient(90deg,#1f2328 0%,#3a3f45 45%,#2a2d31 100%);border-radius:2px}
.cta-band{position:absolute;left:60px;right:60px;bottom:30px;height:8px;background:var(--blue)}
.cta-text{position:absolute;left:0;right:0;top:110px;text-align:center;color:var(--white)}
.cta-text .eyebrow{color:var(--sky)}
.cta-text h2{font-weight:800;font-style:italic;font-size:32px;margin:4px 0 6px}
.cta-text p{font-size:11px;color:#d1d5db;margin-bottom:16px}

/* testimonials */
.testimonials{height:520px;position:relative;padding-top:40px;background:linear-gradient(180deg,var(--white) 70%,var(--mist) 100%)}
.avatar{position:absolute;border-radius:50%;background:linear-gradient(135deg,#d8c3b0,#a9927f);border:4px solid var(--white);box-shadow:0 4px 14px rgba(0,0,0,.15)}
.quote{position:absolute;left:300px;width:600px;top:310px;text-align:center;font-size:11px;color:var(--grey)}
.quote-name{position:absolute;left:0;right:0;top:396px;text-align:center}
.quote-name strong{display:block;color:var(--blue);font-size:15px}
.quote-name span{font-size:10px;color:var(--grey)}
.testimonial-curve{position:absolute;left:0;bottom:0;width:1200px;height:60px}

/* blog */
.blog{height:600px;background:#f1f3f5;padding-top:60px}
.posts{display:flex;justify-content:center;gap:30px;margin-top:34px}
.post{width:340px;background:var(--white);box-shadow:0 4px 16px rgba(0,0,0,.08);text-align:left}
.post-photo{height:200px;position:relative}
.post-date{position:absolute;right:12px;top:12px;width:46px;height:50px;background:var(--blue);color:var(--white);text-align:center;font-weight:700;font-size:18px;line-height:1.2;padding-top:6px}
.post-date small{display:block;font-size:9px;font-weight:500}
.post-body{padding:18px 20px 22px}
.post-body h3{font-size:14px;font-weight:700;line-height:1.3;margin-bottom:8px}
.post-body p{font-size:10px;color:var(--grey);margin-bottom:14px}

/* footer */
.site-footer{height:432px;position:relative;background:var(--dark);color:#cbd5e1;overflow:hidden}
.footer-wave{position:absolute;left:0;top:0;width:1200px;height:90px}
.footer-logo{position:absolute;left:60px;top:150px;display:flex;align-items:center;gap:10px}
.footer-logo .logo-name{color:var(--white)}
.footer-cols{position:absolute;left:330px;top:120px;display:flex}
.footer-col{width:210px}
.footer-col h4{color:var(--white);font-size:14px;font-weight:600;margin-bottom:10px}
.footer-col li{list-style:none;font-size:10px;line-height:2}
.copyright{position:absolute;left:0;right:0;bottom:0;height:44px;border-top:1px solid #23324d;text-align:center;line-height:44px;font-size:10px}
</style>
</head>
<body>

<header class="site-header">
  <div class="topbar">
    <span><svg width="11" height="11" viewBox="0 0 24 24" fill="#fff"><path d="M6.6 10.8a15 15 0 006.6 6.6l2.2-2.2c.3-.3.7-.4 1-.2 1.1.4 2.3.6 3.6.6.6 0 1 .4 1 1V20c0 .6-.4 1-1 1A17 17 0 013 4c0-.6.4-1 1-1h3.5c.6 0 1 .4 1 1 0 1.3.2 2.5.6 3.6.1.3 0 .7-.2 1z"/></svg>Call us today: (555) 014-2290</span>
    <span><svg width="11" height="11" viewBox="0 0 24 24" fill="#fff"><path d="M2 5h20v14H2zm2 2v.5l8 5 8-5V7z"/></svg>info@tavrintelecom.com</span>
    <span><svg width="11" height="11" viewBox="0 0 24 24" fill="#fff"><circle cx="12" cy="12" r="9"/></svg>SUPPORT</span>
    <span>Client Login</span>
  </div>
  <a class="logo" href="#"><span class="logo-dot"></span><span class="logo-name">Tavrin Telecom</span></a>
  <nav class="nav">
    <a class="active" href="#">Home</a><a href="#">Solutions</a><a href="#">Why Tavrin Telecom</a><a href="#">Resources</a><a href="#">Contact</a>
  </nav>
  <a class="btn nav-cta" href="#">Request a Demo</a>
</header>

<section class="hero">
  <div class="hero-photo" role="img" aria-label="Laptop on a desk showing a group video call, office worker seated beside it"></div>
  <div class="hero-text">
    <div class="eyebrow">Any Location, Any Device</div>
    <h1 class="hero-title">GET CONNECTED<br>WITH WORLD</h1>
    <p>Lorem ipsum dolor sit amet, consectetuer adipiscing elit, sed diam nonummy nibh euismod tincidunt.</p>
    <a class="btn" href="#">Get Started</a>
  </div>
  <svg class="hero-curve" viewBox="0 0 1200 90" preserveAspectRatio="none">
    <path d="M0 40 C400 110 800 20 1200 0 L1200 90 L0 90 Z" fill="#0677BA"/>
    <path d="M0 60 C400 120 800 50 1200 40 L1200 90 L0 90 Z" fill="#ffffff"/>
  </svg>
</section>

<section class="services center">
  <div class="eyebrow">Services</div>
  <h2 class="heading">We Provide Best Solutions</h2>
  <p class="lead">Lorem ipsum dolor sit amet, consectetuer adipiscing elit, sed diam nonummy nibh euismod tincidunt ut laoreet dolore magna aliquam erat volutpat.</p>
  <div class="cards">
    <div class="card">
      <svg viewBox="0 0 60 60" fill="none" stroke="#0677BA" stroke-width="2"><rect x="8" y="8" width="16" height="16"/><rect x="36" y="8" width="16" height="16"/><rect x="8" y="36" width="16" height="16"/><rect x="36" y="36" width="16" height="16"/><path d="M24 16h12M16 24v12M44 24v12M24 44h12"/></svg>
      <h3>UCaaS</h3><p>Lorem ipsum dolor sit amet, consectetuer adipiscing elit, sed diam nonummy nibh euismod ut.</p><a class="more" href="#">Learn More</a>
    </div>
    <div class="card">
      <svg viewBox="0 0 60 60" fill="none" stroke="#0677BA" stroke-width="2"><rect x="10" y="10" width="40" height="28"/><path d="M22 48h16M30 38v10"/><path d="M18 30l8-8 6 6 10-10"/></svg>
      <h3>SD-WAN</h3><p>Lorem ipsum dolor sit amet, consectetuer adipiscing elit, sed diam nonummy nibh euismod ut.</p><a class="more" href="#">Learn More</a>
    </div>
    <div class="card featured">
      <svg viewBox="0 0 60 60" fill="none" stroke="#fff" stroke-width="2"><rect x="8" y="12" width="44" height="30" rx="4"/><path d="M18 42l-4 10 12-10"/><path d="M18 24h24M18 31h16"/></svg>
      <h3>Business SMS/MMS</h3><p>Lorem ipsum dolor sit amet, consectetuer adipiscing elit, sed diam nonummy nibh euismod ut.</p><a class="more" href="#">Learn More</a>
    </div>
    <div class="card">
      <svg viewBox="0 0 60 60" fill="none" stroke="#0677BA" stroke-width="2"><rect x="8" y="16" width="32" height="28" rx="3"/><path d="M40 26l12-8v24l-12-8z"/></svg>
      <h3>Video Conferencing</h3><p>Lorem ipsum dolor sit amet, consectetuer adipiscing elit, sed diam nonummy nibh euismod ut.</p><a class="more" href="#">Learn More</a>
    </div>
    <div class="card">
      <svg viewBox="0 0 60 60" fill="none" stroke="#0677BA" stroke-width="2"><circle cx="30" cy="14" r="6"/><circle cx="12" cy="46" r="6"/><circle cx="48" cy="46" r="6"/><path d="M30 20v12M30 32L14 41M30 32l16 9"/></svg>
      <h3>Managed Network</h3><p>Lorem ipsum dolor sit amet, consectetuer adipiscing elit, sed diam nonummy nibh euismod ut.</p><a class="more" href="#">Learn More</a>
    </div>
  </div>
  <a class="btn" href="#">View All Services</a>
</section>

<section class="about">
  <svg style="position:absolute;left:0;top:0" width="1200" height="520" viewBox="0 0 1200 520">
    <path d="M0 0 L1200 0 L1200 20 C800 70 400 0 0 40 Z" fill="#ffffff"/>
    <path d="M0 470 C400 430 800 520 1200 480 L1200 520 L0 520 Z" fill="#ffffff"/>
    <path d="M0 500 C300 470 600 520 800 500" stroke="#0677BA" stroke-width="6" fill="none"/>
  </svg>
  <div class="about-photo" role="img" aria-label="Smiling support agent wearing a headset"></div>
  <div class="about-text">
    <div class="eyebrow">About Us</div>
    <h2 class="heading">We Are Tavrin Telecom</h2>
    <p>Tavrin Telecom provides hosted PBX service from small business to the enterprise customer with a unique pricing model to easily meet your telecom bills.</p>
    <p>Lorem ipsum dolor sit amet, consectetuer adipiscing elit, sed diam nonummy nibh euismod tincidunt ut laoreet dolore magna aliquam erat volutpat. Ut wisi enim ad minim veniam, quis nostrud exerci tation ullamcorper suscipit lobortis nisl ut aliquip ex ea commodo consequat.</p>
    <a class="btn" href="#">Learn More</a>
  </div>
</section>

<section class="features center">
  <div class="eyebrow">Why Choose Us</div>
  <h2 class="heading">Key Facts &amp; Features</h2>
  <p class="lead">Lorem ipsum dolor sit amet, consectetuer adipiscing elit, sed diam nonummy nibh euismod tincidunt ut laoreet dolore magna aliquam erat volutpat.</p>
  <div class="feature-row">
    <div class="feature">
      <div class="feature-icon"><svg width="48" height="48" viewBox="0 0 48 48" fill="none" stroke="#0054AA" stroke-width="2"><circle cx="24" cy="24" r="8"/><path d="M24 4v10M24 34v10M4 24h10M34 24h10"/></svg></div>
      <h3>Integrated Solutions</h3><p>Lorem ipsum dolor sit amet, consectetuer adipiscing elit, sed diam nonummy nibh euismod.</p>
    </div>
    <div class="feature">
      <div class="feature-icon"><svg width="48" height="48" viewBox="0 0 48 48" fill="none" stroke="#0054AA" stroke-width="2"><rect x="8" y="12" width="32" height="24" rx="3"/><path d="M8 20h32"/><circle cx="30" cy="29" r="3"/></svg></div>
      <h3>Fixed Monthly Cost</h3><p>Lorem ipsum dolor sit amet, consectetuer adipiscing elit, sed diam nonummy nibh euismod.</p>
    </div>
    <div class="feature">
      <div class="feature-icon"><svg width="48" height="48" viewBox="0 0 48 48" fill="none" stroke="#0054AA" stroke-width="2"><circle cx="24" cy="24" r="18"/><path d="M6 24h36M24 6c-8 8-8 28 0 36M24 6c8 8 8 28 0 36"/></svg></div>
      <h3>Global Reliability</h3><p>Lorem ipsum dolor sit amet, consectetuer adipiscing elit, sed diam nonummy nibh euismod.</p>
    </div>
    <div class="feature">
      <div class="feature-icon"><svg width="48" height="48" viewBox="0 0 48 48" fill="none" stroke="#0054AA" stroke-width="2"><path d="M10 28v-6a14 14 0 0128 0v6"/><rect x="6" y="26" width="8" height="12" rx="2"/><rect x="34" y="26" width="8" height="12" rx="2"/></svg></div>
      <h3>24/7 Support</h3><p>Lorem ipsum dolor sit amet, consectetuer adipiscing elit, sed diam nonummy nibh euismod.</p>
    </div>
  </div>
</section>

<section class="cta">
  <div class="cta-photo" role="img" aria-label="Dark-toned photo of a desk with a laptop and smartphone"></div>
  <div class="cta-band"></div>
  <div class="cta-text">
    <div class="eyebrow">Contact Us</div>
    <h2>Want To Know More! Get In Touch With Us</h2>
    <p>Lorem ipsum dolor sit amet, consectetuer.</p>
    <a class="btn" href="#">Contact Us Now</a>
  </div>
</section>

<section class="testimonials center">
  <div class="eyebrow">Testimonials</div>
  <h2 class="heading">What Happy Clients say</h2>
  <div class="avatar" role="img" aria-label="Client portrait" style="left:160px;top:130px;width:54px;height:54px"></div>
  <div class="avatar" role="img" aria-label="Client portrait" style="left:100px;top:230px;width:44px;height:44px"></div>
  <div class="avatar" role="img" aria-label="Client portrait" style="left:170px;top:320px;width:62px;height:62px"></div>
  <div class="avatar" role="img" aria-label="Client portrait" style="left:550px;top:160px;width:100px;height:100px"></div>
  <div class="avatar" role="img" aria-label="Client portrait" style="left:920px;top:130px;width:50px;height:50px"></div>
  <div class="avatar" role="img" aria-label="Client portrait" style="left:1010px;top:230px;width:58px;height:58px"></div>
  <div class="avatar" role="img" aria-label="Client portrait" style="left:950px;top:330px;width:42px;height:42px"></div>
  <p class="quote">“Lorem ipsum dolor sit amet, consectetuer adipiscing elit, sed diam nonummy nibh euismod tincidunt ut laoreet dolore magna aliquam erat volutpat. Ut wisi enim ad minim veniam, quis nostrud exerci tation ullamcorper suscipit lobortis nisl ut aliquip ex ea commodo consequat. Duis autem vel eum iriure dolor in hendrerit in vulputate velit esse molestie consequat.”</p>
  <div class="quote-name"><strong>John Doe</strong><span>CEO, Company Name</span></div>
  <svg class="testimonial-curve" viewBox="0 0 1200 60" preserveAspectRatio="none">
    <path d="M0 60 C300 20 600 60 1200 30 L1200 60 Z" fill="#f1f3f5"/>
    <path d="M0 60 C300 20 600 60 1200 30" stroke="#0677BA" stroke-width="4" fill="none"/>
  </svg>
</section>

<section class="blog center">
  <div class="eyebrow">News Updates</div>
  <h2 class="heading">Latest Blog Posts</h2>
  <div class="posts">
    <article class="post">
      <div class="post-photo" role="img" aria-label="Team working at laptops in a bright office" style="background:linear-gradient(135deg,#dfe6ee,#9fb3c8)"><div class="post-date">28<small>Jun</small></div></div>
      <div class="post-body"><h3>Lorem ipsum dolor sit amet, consectetuer adipiscing</h3><p>Lorem ipsum dolor sit amet, consectetuer adipiscing elit, sed diam nonummy nibh euismod tincidunt.</p><a class="btn" href="#">Learn More</a></div>
    </article>
    <article class="post">
      <div class="post-photo" role="img" aria-label="Overhead view of colleagues meeting around a wooden table" style="background:linear-gradient(135deg,#6b4f3a,#2c2520)"><div class="post-date">28<small>Jun</small></div></div>
      <div class="post-body"><h3>Lorem ipsum dolor sit amet, consectetuer adipiscing</h3><p>Lorem ipsum dolor sit amet, consectetuer adipiscing elit, sed diam nonummy nibh euismod tincidunt.</p><a class="btn" href="#">Learn More</a></div>
    </article>
    <article class="post">
      <div class="post-photo" role="img" aria-label="Hands holding a smartphone beside a laptop" style="background:linear-gradient(135deg,#e9d8c8,#b99a80)"><div class="post-date">28<small>Jun</small></div></div>
      <div class="post-body"><h3>Lorem ipsum dolor sit amet, consectetuer adipiscing</h3><p>Lorem ipsum dolor sit amet, consectetuer adipiscing elit, sed diam nonummy nibh euismod tincidunt.</p><a class="btn" href="#">Learn More</a></div>
    </article>
  </div>
</section>

<footer class="site-footer">
  <svg class="footer-wave" viewBox="0 0 1200 90" preserveAspectRatio="none">
    <path d="M0 0 L1200 0 L1200 30 C800 90 400 10 0 60 Z" fill="#f1f3f5"/>
    <path d="M0 60 C400 10 800 90 1200 30 L1200 40 C800 100 400 22 0 70 Z" fill="#0677BA"/>
  </svg>
  <div class="footer-logo"><span class="logo-dot"></span><span class="logo-name">Tavrin Telecom</span></div>
  <div class="footer-cols">
    <div class="footer-col"><h4>Useful Links</h4><ul><li>Home</li><li>Solutions</li><li>Why Tavrin Telecom</li><li>Resources</li><li>Contact</li></ul></div>
    <div class="footer-col"><h4>Solutions</h4><ul><li>UCaaS</li><li>SD-WAN</li><li>Business SMS/MMS</li><li>Video Conferencing</li><li>Managed Network</li></ul></div>
    <div class="footer-col"><h4>Support</h4><ul><li>Help</li><li>FAQ</li><li>Privacy Policy</li><li>Terms &amp; Conditions</li></ul></div>
    <div class="footer-col"><h4>Contact</h4><ul><li>Phone:</li><li>(555) 014-2290</li><li>Mail:</li><li>info@tavrintelecom.com</li></ul></div>
  </div>
  <div class="copyright">© Tavrin Telecom - 2022, All Rights Reserved.</div>
</footer>

</body>
</html>
```